About us:
Looking for eye catching cards for our 4D/HD Ultrasound Studio.

Description:
We are the premier 4D/HD Ultrasound studio in Pensacola/Pace as well as the greater panhandle area. We are a 4D/HD Ultrasound Studio in Pace, Florida, just a few minutes north of Pensacola. We offer 4D/HD imagining an early gender determination, 8 weeks by blood test and 14 weeks by ultrasound. We utilize the latest in 4D/HD technology to render beautiful images and memories that will last a lifetime.

At 4D Tiny Glimpse of Pace, we give a whole new meaning to ultrasounds. We utilize the most up-to-date 4D/HD ultrasound imaging, so we can provide clear, amazing images of your unborn baby to life. Will she have your nose or her Daddy's smile? Book your appointment today for an unforgettable experience. We also offer heartbeat animals.

Phone: 8507149350
www.4dtinyglimpse.example
address: 7816 -B HWY 213
Pace, FL 32904

Target Market(s)

Pregnant women

Requirements
Should not have
• Ultrasound training

```html
<!DOCTYPE html>
<html lang="en">
<head>
<meta charset="utf-8">
<title>Pensacola 4D HD Ultrasound – Trifold Brochure</title>
<link rel="stylesheet" href="https://fonts.googleapis.com/css2?family=Open+Sans:wght@400;600;700&family=Montserrat:wght@800&display=swap">
<style>
:root{
  --coral:#d9665f;
  --coral-soft:#e58f88;
  --blush:#f2c9c3;
  --teal:#4db5c5;
  --teal-text:#3aa7b7;
  --price:#e2508c;
  --paper:#f7f6f6;
  --ink:#3d3d3d;
  --ink-soft:#6a6a6a;
  --stage:#c9c8cc;
}
*{box-sizing:border-box;margin:0;padding:0}
html,body{width:1200px;height:2755px;overflow:hidden}
body{background:var(--stage);font-family:"Open Sans",Arial,sans-serif;color:var(--ink);position:relative}
.section-label{position:absolute;font-family:"Montserrat",Arial,sans-serif;font-weight:800;font-size:42px;color:#111}
.sheet{position:absolute;background:var(--paper);overflow:hidden;box-shadow:0 8px 24px rgba(0,0,0,.25)}
.panel{position:absolute;top:0;bottom:0;overflow:hidden}
.fold{position:absolute;top:0;bottom:0;width:1px;background:rgba(0,0,0,.08)}
.waves{position:absolute;left:0;width:100%}
.photo{position:absolute}

/* cover panel */
.cover-photo{background:linear-gradient(160deg,#f4ecea 0%,#e9cfc9 35%,#d9a9a2 60%,#c98f8a 100%)}
.cover-tint{position:absolute;inset:0;background:linear-gradient(90deg,rgba(217,102,95,.35),rgba(217,102,95,0) 60%)}
.cover-title{position:absolute;background:var(--coral);color:#fff;font-weight:600;line-height:1.22;padding:14px 20px}

/* outside left */
.gallery{position:absolute;display:grid;grid-template-columns:1fr 1fr;gap:12px}
.gallery .shot{height:100px;border:5px solid #fff;box-shadow:0 2px 6px rgba(0,0,0,.35);background:radial-gradient(circle at 45% 45%,#d99a6e 0%,#a55a36 45%,#3b1a10 100%)}
.small-copy{font-size:12px;line-height:1.45;color:var(--ink)}
.book-title{color:var(--teal-text);font-size:30px;line-height:1.05;font-weight:400;margin:12px 0 8px}
.fine{font-size:9.5px;line-height:1.4;color:var(--ink-soft);margin-bottom:5px}

/* contact */
.contact{position:absolute;text-align:center}
.contact .rule{height:1px;background:var(--coral);margin:10px 0}
.contact .addr{font-size:26px;line-height:1.15;color:#2a2a2a;font-weight:600}
.contact .web{font-size:17px;font-weight:700;color:#333;margin-top:16px}

/* inside */
.inside-title{color:var(--teal-text);font-weight:400;font-size:26px;line-height:1.1}
.body-copy{font-size:10.5px;line-height:1.5;color:var(--ink)}
.bold-copy{font-size:14px;line-height:1.4;font-weight:700;color:#222}
.note-box{background:var(--coral);color:#fff;font-size:8px;line-height:1.45;border-radius:10px;padding:10px 12px;margin-top:12px}

.prices{position:absolute}
.price-row{margin-bottom:9px}
.price-head{display:flex;justify-content:space-between;align-items:center;background:#ececec;font-size:11.5px;font-weight:700;padding:2px 0 2px 6px}
.price-head .tag{background:var(--price);color:#fff;font-size:11px;font-weight:600;padding:2px 10px;min-width:74px;text-align:center}
.price-sub{display:grid;grid-template-columns:1fr 1.2fr 1fr;font-size:6.5px;color:#555;border-bottom:1px solid #ddd}
.price-sub span{padding:3px 4px;border-bottom:1px solid #e6e6e6}
.closing{font-size:10.5px;color:var(--teal-text);line-height:1.4;margin-top:12px}
.gift{font-size:13px;font-style:italic;font-weight:700;color:var(--teal-text);margin-top:12px}
</style>
</head>
<body>

<!-- COVER -->
<div class="section-label" style="left:90px;top:780px">Cover Outside</div>
<div class="sheet" style="left:500px;top:40px;width:340px;height:790px">
  <div class="photo cover-photo" role="img" aria-label="Photo of a pregnant belly with a hand resting on it" style="left:0;top:0;width:340px;height:620px"></div>
  <div class="cover-tint"></div>
  <svg class="waves" style="top:0;height:40px" viewBox="0 0 340 40" preserveAspectRatio="none"><polygon points="0,0 340,0 340,14 0,30" fill="var(--coral)"/></svg>
  <div class="cover-title" style="left:40px;top:400px;width:290px;font-size:28px">Pensacola,<br>FL - 4D<br>HD Ultrasound</div>
  <svg class="waves" style="bottom:0;height:230px" viewBox="0 0 340 230" preserveAspectRatio="none">
    <path d="M0,40 C110,10 230,10 340,30 L340,230 L0,230Z" fill="var(--coral-soft)"/>
    <path d="M0,60 C110,30 230,30 340,50 L340,230 L0,230Z" fill="var(--coral)"/>
    <path d="M0,190 C120,130 240,120 340,110 L340,230 L0,230Z" fill="var(--teal)"/>
  </svg>
</div>

<!-- OUTSIDE -->
<div class="section-label" style="left:820px;top:935px">Outside</div>
<div class="sheet" style="left:120px;top:1010px;width:960px;height:720px">
  <svg class="waves" style="top:0;height:34px" viewBox="0 0 960 34" preserveAspectRatio="none"><polygon points="0,0 960,0 960,30 0,14" fill="var(--coral)"/></svg>

  <div class="panel" style="left:0;width:320px">
    <div class="gallery" role="img" aria-label="Four 3D ultrasound photos of a baby" style="left:28px;top:40px;width:250px">
      <div class="shot"></div><div class="shot"></div><div class="shot"></div><div class="shot"></div>
    </div>
    <div style="position:absolute;left:28px;top:280px;width:270px">
      <p class="small-copy">Take a peek at our Photo Gallery. All of our 2D, 3D, 4D, HD elective ultrasound images are truly ours. They come directly off our machine from our highly trained staff.</p>
      <p class="small-copy" style="margin-top:6px">We can start getting great 3D/4D images as early as 8 weeks!</p>
      <h2 class="book-title">Book your<br>ultrasound online</h2>
      <p class="fine">Please note that our 2D ultrasounds and 4D ultrasounds can only be performed on pregnant women who are under the care of a physician.</p>
      <p class="fine">Please call one of our 3D 4D HD facilities should you have any questions regarding 3D or 4D ultrasound or if you need to make an appointment.</p>
    </div>
  </div>
  <div class="fold" style="left:320px"></div>

  <div class="panel" style="left:320px;width:320px">
    <div class="contact" style="left:30px;top:330px;width:260px">
      <div class="rule"></div>
      <p class="addr">7816-B Hwy 213<br>Pace, FL 32904<br>(850) 714-9350</p>
      <div class="rule"></div>
      <p class="web">www.4dtinyglimpse.example</p>
    </div>
  </div>
  <div class="fold" style="left:640px"></div>

  <div class="panel" style="left:640px;width:320px">
    <div class="photo cover-photo" role="img" aria-label="Photo of a pregnant belly with a hand resting on it" style="left:0;top:30px;width:320px;height:560px"></div>
    <div class="cover-tint"></div>
    <div class="cover-title" style="left:30px;top:420px;width:270px;font-size:25px">Pensacola,<br>FL - 4D<br>HD Ultrasound</div>
  </div>

  <svg class="waves" style="bottom:0;height:210px" viewBox="0 0 960 210" preserveAspectRatio="none">
    <path d="M0,112 C260,150 560,130 960,40 L960,210 L0,210Z" fill="var(--coral-soft)"/>
    <path d="M0,126 C260,166 560,150 960,60 L960,210 L0,210Z" fill="var(--coral)"/>
    <path d="M0,165 C260,205 600,200 960,150 L960,210 L0,210Z" fill="var(--teal)"/>
  </svg>
</div>

<!-- INSIDE -->
<div class="section-label" style="left:90px;top:1860px">Inside</div>
<div class="sheet" style="left:110px;top:1920px;width:960px;height:800px">
  <svg class="waves" style="top:0;height:60px" viewBox="0 0 960 60" preserveAspectRatio="none">
    <path d="M0,0 L960,0 L960,30 C700,0 300,10 0,50Z" fill="var(--teal)"/>
    <path d="M0,30 C300,0 700,-5 960,40 L960,50 C700,10 300,12 0,50Z" fill="var(--coral)"/>
  </svg>

  <div class="panel" style="left:0;width:320px">
    <div class="photo" role="img" aria-label="Photo of an expecting couple holding an ultrasound print" style="left:22px;top:40px;width:276px;height:166px;background:linear-gradient(120deg,#efe7e3,#d9b8a8 50%,#f2ece8)"></div>
    <div style="position:absolute;left:22px;top:228px;width:282px">
      <h2 class="inside-title">Pensacola,<br>FL - 4D HD Ultrasound</h2>
      <p class="body-copy" style="margin-top:16px">4D Tiny Glimpse of Pensacola offers the finest 3D/4D HD prenatal ultrasound experience available. Combining cutting-edge technology with a spa &amp; theater environment, we bring unbelievable images of your unborn baby to life!</p>
      <p class="bold-copy" style="margin-top:16px">We can tell if you are having a little boy or a little girl starting at 14 Weeks!!!<br>We offer the finest HD Live ultrasounds with the use of our Solvance ultrasound machine.</p>
    </div>
  </div>
  <div class="fold" style="left:320px"></div>

  <div class="panel" style="left:320px;width:320px">
    <div class="photo" role="img" aria-label="Photo of a mother and little girl in a sunny field" style="left:14px;top:40px;width:292px;height:166px;background:linear-gradient(135deg,#f0d48a,#c89a4a 45%,#8b6b2c 75%,#d9c46a)"></div>
    <div style="position:absolute;left:14px;top:228px;width:292px">
      <h2 class="inside-title">Our Studio</h2>
      <p class="body-copy" style="margin-top:4px;font-size:9.5px">4D Tiny Glimpse of Pensacola was started because I wanted to give others the breathtaking experience of seeing their unborn child just like I did with mine while they were still in the womb. I have been blessed enough to be able to share this with mothers everyday!</p>
      <div class="note-box">4D Tiny Glimpse of Pensacola Ultrasound is family owned and operated. We have kept our studio very welcoming and comfortable unlike other studios that look like sterile bleak medical offices. We believe that your experience should be warm and inviting since you will soon be inviting your unborn into this wonderful world.</div>
      <div class="note-box">From a yawn to a hiccup or stretch, your ultrasound will allow you to take a sneak peek at your unborn child in the womb. We only use state of the art 3D 4D HD Live ultrasound machines to ensure you get the best images of your unborn baby. Our goal is to ensure that you have the best experience possible.</div>
      <div class="note-box">We are a warm and inviting studio and welcome all of your family, friends, and children. We believe that children should be a part of this wonderful experience so they feel like a part of the family at all times. We have a large theater-like viewing room with seating for up to 10 people and plenty of toys to keep little ones busy.</div>
    </div>
  </div>
  <div class="fold" style="left:640px"></div>

  <div class="panel" style="left:640px;width:320px">
    <h2 class="inside-title" style="position:absolute;left:14px;top:40px">Ultrasound<br>Packages &amp; Prices</h2>
    <div class="prices" style="left:14px;top:115px;width:292px">
      <div class="price-row"><div class="price-head">Early Gender DNA Test<span class="tag">$129.00</span></div>
        <div class="price-sub"><span>Starting at 8 Weeks</span><span>Results in 2 Days</span><span>Results in 1 Day ($20)</span></div></div>
      <div class="price-row"><div class="price-head">2D Heartbeat<span class="tag">$65.00</span></div>
        <div class="price-sub"><span>2D Scan</span><span>Listen to your Baby's Heartbeat</span><span>Printed Images</span></div></div>
      <div class="price-row"><div class="price-head">2D Gender Peek<span class="tag">$90.00</span></div>
        <div class="price-sub"><span>2D Scan</span><span>Gender Determination (14+ Weeks)</span><span>Baby's Heartbeat</span><span>Printed Images</span><span>Images on BabyReel App</span><span>$10 OFF Future Visit</span></div></div>
      <div class="price-row"><div class="price-head">Mid-Week 4D/HD Peek<span class="tag">$115.00</span></div>
        <div class="price-sub"><span>4D/HD Scan</span><span>Gender Determination (14+ Weeks)</span><span>Baby's Heartbeat</span><span>Printed Images</span><span>Images on BabyReel App</span><span>$10 OFF Future Visit</span></div></div>
      <div class="price-row"><div class="price-head">4D/HD Deluxe Peek<span class="tag">$155.00</span></div>
        <div class="price-sub"><span>4D/HD Scan</span><span>Gender Determination (14+ Weeks)</span><span>Baby's Heartbeat</span><span>Printed Images</span><span>Images on BabyReel App</span><span>$15 OFF Future Visit</span></div></div>
      <div class="price-row"><div class="price-head">4D/HD Premium Peek<span class="tag">$185.00</span></div>
        <div class="price-sub"><span>4D/HD Scan</span><span>Gender Determination (14+ Weeks)</span><span>Baby's Heartbeat</span><span>Printed Images</span><span>Video of Session on BabyReel</span><span>Images on BabyReel App</span><span>$20 OFF Future Visit</span><span></span><span></span></div></div>
      <div class="price-row"><div class="price-head">4D/HD Double Peek<span class="tag">$299.00</span></div>
        <div class="price-sub"><span>Gender Determination (14+ Weeks)</span><span>Listen to your Baby's Heartbeat</span><span>Printed Images</span><span>Video of Session on BabyReel</span><span>Images on BabyReel App</span><span>$20 OFF Future Visit</span></div></div>
      <p class="closing">It is our pleasure to share the experience of your pregnancy with you.</p>
      <p class="gift">GIFT CERTIFICATES AVAILABLE!</p>
    </div>
  </div>

  <svg class="waves" style="bottom:0;height:150px" viewBox="0 0 960 150" preserveAspectRatio="none">
    <path d="M0,10 C80,90 200,100 420,90 C640,80 820,60 960,30 L960,150 L0,150Z" fill="var(--coral)"/>
    <path d="M0,60 C100,120 260,120 480,115 C700,110 840,95 960,75 L960,150 L0,150Z" fill="var(--teal)"/>
  </svg>
</div>

</body>
</html>
```